Exciting new aperitif brand needs a great label

Vel-Orin is a wonderful rich new premium-priced bitter aperitif, with a deep red colour, from a 100+ year old distillery (1890) near Turin in the Piedmont region of Italy. Inspired by Torvesi, it is perfectly formulated to elevate the classic Baldetti cocktail (and variations on it). It also goes perfectly in a Spritz or a long mixed drink with soda or tonic. The name Vel-Orin is derived from the French for 'peak' and the Italian word for 'love'.

The label, which should take inspiration from Torvesi, but be distinctively different, can incoporate any number of premium label embellishments (foil, embossing, textures etc) and should be no greater than 11cm (height) x 9cm (width) with any core imagery restricted to a width of c.7cm.

The attached mood board should act as inspiration and colour should largely be restricted to reds, blues, whites and perhaps orange. For completeness, the label should note that the ABV is 25% and the bottle size 70cl.

Target Market(s)

21-45yr olds - equal split female/male

Colors
0054AA
0677BA
7BADD7
CADEEF
E8F1F8
0094D4
00A9DD
6FCCEA
C7EBF8
E9F6FB
EE7325
F08F49
F5BC92
FAE3D3
FDF4ED
EB3D1F
EC4F4E
F09395
F8D3D4
FCEDEE

Requirements
Must have
• Great lettering design on the name Vel-Orin

```html
<!DOCTYPE html>
<html lang="en">
<head>
<meta charset="utf-8">
<title>Vel-Orin aperitif label</title>
<link rel="stylesheet" href="https://fonts.googleapis.com/css2?family=Limelight&family=Abril+Fatface&display=swap">
<style>
  :root {
    --ink-blue: #00349b;
    --signal-red: #ec3a22;
    --cream: #f4f2ea;
    --bevel-grey: #d4d8de;
    --paper: #f1f1f0;
    --label-white: #ffffff;
    --wave-tint: #f3f7fb;
  }
  html, body {
    margin: 0;
    width: 1200px;
    height: 1200px;
    overflow: hidden;
    background: var(--paper);
  }
  .label-art {
    display: block;
    width: 1200px;
    height: 1200px;
  }
  .brand-name {
    font-family: "Limelight", sans-serif;
    font-size: 136px;
  }
  .brand-name-shadow { fill: var(--signal-red); }
  .brand-name-bevel { fill: var(--bevel-grey); }
  .brand-name-face { fill: var(--cream); }
  .spec-text {
    font-family: "Abril Fatface", serif;
    font-size: 26px;
    fill: var(--ink-blue);
  }
</style>
</head>
<body>
<svg class="label-art" viewBox="0 0 1200 1200" xmlns="http://www.w3.org/2000/svg">
  <defs>
    <pattern id="hatch" width="10" height="10" patternUnits="userSpaceOnUse" patternTransform="rotate(45)">
      <rect width="10" height="10" fill="var(--label-white)"/>
      <rect width="3" height="10" fill="var(--ink-blue)"/>
    </pattern>
  </defs>

  <!-- outer hatched frame -->
  <g class="outer-frame">
    <rect x="293" y="227" width="614" height="745" fill="url(#hatch)" stroke="var(--ink-blue)" stroke-width="5"/>
    <rect x="308" y="242" width="584" height="715" fill="var(--label-white)" stroke="var(--ink-blue)" stroke-width="2"/>
    <rect x="313" y="247" width="574" height="705" fill="none" stroke="var(--ink-blue)" stroke-width="4" stroke-dasharray="1 2"/>
    <rect class="wave-field" role="img" aria-label="Faint wave pattern background" x="319" y="253" width="562" height="693" fill="var(--wave-tint)" stroke="var(--ink-blue)" stroke-width="2"/>
  </g>

  <!-- corner squares -->
  <g class="corner-squares" fill="var(--label-white)" stroke="var(--ink-blue)" stroke-width="3">
    <rect x="309" y="243" width="27" height="28"/>
    <rect x="864" y="243" width="27" height="28"/>
    <rect x="309" y="928" width="27" height="28"/>
    <rect x="864" y="928" width="27" height="28"/>
  </g>

  <!-- regional flag -->
  <rect class="region-flag" role="img" aria-label="Regional flag of Piedmont" x="560" y="323" width="81" height="49" fill="var(--signal-red)" stroke="var(--ink-blue)" stroke-width="3"/>

  <!-- central name band -->
  <g class="name-band">
    <rect x="296" y="442" width="608" height="316" fill="var(--cream)" stroke="var(--ink-blue)" stroke-width="3"/>
    <rect x="302" y="450" width="596" height="299" fill="var(--ink-blue)"/>
    <rect x="311" y="458" width="578" height="283" fill="none" stroke="var(--label-white)" stroke-width="2"/>

    <g class="stepped-frame" fill="none" stroke="var(--signal-red)" stroke-width="1.5">
      <path d="M355 469 H845 V500 H877 V698 H845 V730 H355 V698 H322 V500 H355 Z"/>
      <path d="M362 476 H838 V508 H870 V690 H838 V723 H362 V690 H329 V508 H362 Z"/>
    </g>

    <g class="corner-diamonds" fill="var(--signal-red)">
      <rect x="331" y="476" width="12" height="12" transform="rotate(45 338 483)"/>
      <rect x="854" y="476" width="12" height="12" transform="rotate(45 861 483)"/>
      <rect x="331" y="709" width="12" height="12" transform="rotate(45 338 716)"/>
      <rect x="854" y="709" width="12" height="12" transform="rotate(45 861 716)"/>
    </g>

    <g class="name-oval" stroke="var(--signal-red)" stroke-width="1.5">
      <ellipse cx="600" cy="599" rx="277" ry="129" fill="var(--ink-blue)"/>
      <ellipse cx="600" cy="599" rx="271" ry="123" fill="none"/>
    </g>

    <g class="brand-name" text-anchor="middle">
      <text class="brand-name-shadow" x="604" y="650" textLength="452" lengthAdjust="spacingAndGlyphs">VEL-ORIN</text>
      <text class="brand-name-bevel" x="601" y="648" textLength="452" lengthAdjust="spacingAndGlyphs">VEL-ORIN</text>
      <text class="brand-name-face" x="600" y="647" textLength="452" lengthAdjust="spacingAndGlyphs">VEL-ORIN</text>
    </g>
  </g>

  <!-- specifications -->
  <g class="specs">
    <text class="spec-text" x="512" y="866" text-anchor="middle" textLength="165" lengthAdjust="spacingAndGlyphs">ABV 25%</text>
    <line x1="634" y1="827" x2="634" y2="888" stroke="var(--ink-blue)" stroke-width="1.5"/>
    <text class="spec-text" x="722" y="866" text-anchor="middle" textLength="96" lengthAdjust="spacingAndGlyphs">70CL</text>
  </g>
</svg>
</body>
</html>
```